SilverLedgerOak - Double Sided Business Card

We are looking for design options or our business cards. We are a Business Solutions and HR solutions Provider - the theme is business, for this card.

Our brand colours are represented within our logo.

Details needed to be put on the front of the business card are:

Employees name: [Sample Name]
Role: [Sample Role]

Address: Suite 4 - Level 3/48 Halloran Avenue Parramatta NSW 2150
M: 0000 000 000
P: 1300 847 213
F: 1300 847 286
E: sample@silverledgeroak.com.au
www.silverledgeroak.com.au
Updates

Reason: Hello, could we please increase our deadline by 5 days. Thanking you, Tess

Target Market(s)

Business Owners, also Candidates looking for Employment

Industry/Entity Type

Business

Contact Information for Business Card

Role: [Sample Role]

M: 0000 000 000
P: 1300 847 213
F: 1300 847 286

Font styles to use
Sans Serif

Colors
3276b5
3176b5
0455a3
85abd2
cfdeed
ffffff
000000
1b1b1b
757575

Requirements
Must have
• Details needed to be put on the front of the business card are:
• Employees name: [Sample Name]
• Role: [Sample Role]
• Address: Suite 4 - Level 3/48 Halloran Avenue Parramatta NSW 2150
• M: 0000 000 000
• P: 1300 847 213
• F: 1300 847 286
• E: sample@silverledgeroak.com.au
• www.silverledgeroak.com.au
Nice to have
• Simplicity, clean and professional.

```html
<!DOCTYPE html>
<html lang="en">
<head>
<meta charset="utf-8">
<title>SilverLedgerOak – Business Card</title>
<link href="https://fonts.googleapis.com/css2?family=Open+Sans:wght@400;600;700&family=Roboto:wght@700&display=swap" rel="stylesheet">
<style>
  :root {
    --page: #e9ebee;
    --white: #ffffff;
    --brand-blue: #0455a3;
    --brand-mid: #3276b5;
    --brand-light: #85abd2;
    --navy: #0b1c34;
    --navy-deep: #06111f;
    --ink: #1b1b1b;
    --muted: #757575;
  }
  * { box-sizing: border-box; margin: 0; padding: 0; }
  html, body { width: 1200px; height: 874px; overflow: hidden; }
  body {
    background: var(--page);
    font-family: "Open Sans", Arial, sans-serif;
    position: relative;
  }
  .card {
    position: absolute;
    width: 540px;
    height: 306px;
    overflow: hidden;
    box-shadow: 0 4px 14px rgba(0,0,0,.18);
  }
  .card--front { left: 45px; top: 80px; background: var(--white); }
  .card--back { left: 615px; top: 80px; background: radial-gradient(ellipse at 50% 40%, #13294a 0%, var(--navy) 55%, var(--navy-deep) 100%); }
  .card--back-alt { left: 330px; top: 468px; background: linear-gradient(135deg, #0a2347 0%, #123a72 45%, #1d539c 100%); }

  /* Front */
  .brand {
    position: absolute; left: 14px; top: 88px; width: 246px;
    display: flex; flex-direction: column; align-items: center;
  }
  .brand__mark { width: 34px; height: 34px; background: var(--brand-blue); margin-bottom: 12px; }
  .brand__name {
    font-family: "Roboto", Arial, sans-serif; font-weight: 700;
    font-size: 25px; color: var(--brand-blue); letter-spacing: .3px;
  }
  .brand__tagline {
    margin-top: 6px; font-size: 8.4px; font-weight: 700; color: var(--ink);
    border-top: 1px solid var(--ink); padding-top: 3px; white-space: nowrap;
  }
  .contact { position: absolute; left: 298px; top: 42px; color: var(--ink); }
  .contact__name { font-size: 17px; font-weight: 700; color: var(--brand-blue); line-height: 1.2; }
  .contact__role { font-size: 12.5px; margin-bottom: 14px; }
  .contact__list { list-style: none; }
  .contact__item { display: flex; align-items: center; font-size: 12.5px; height: 19px; }
  .contact__icon { width: 13px; height: 13px; margin-right: 8px; flex: none; }
  .contact__company { margin-top: 12px; font-size: 12.5px; font-weight: 700; color: var(--brand-blue); }
  .contact__address { font-size: 12.5px; line-height: 1.4; }
  .bands { position: absolute; left: 0; bottom: 0; }

  /* Backs */
  .back__name {
    position: absolute; left: 0; right: 0; top: 108px; text-align: center;
    font-family: "Roboto", Arial, sans-serif; font-weight: 700;
    font-size: 30px; color: var(--white); letter-spacing: .5px;
  }
  .social { position: absolute; left: 0; right: 0; top: 212px; display: flex; justify-content: center; gap: 6px; }
  .social__dot { width: 17px; height: 17px; border: 1.5px solid var(--white); border-radius: 50%; }
  .web {
    position: absolute; left: 0; right: 0; top: 238px;
    display: flex; align-items: center; justify-content: center; gap: 12px;
    color: var(--white); font-size: 13px; letter-spacing: 2px;
  }
  .web__rule { width: 90px; height: 1px; background: linear-gradient(90deg, transparent, var(--brand-mid)); }
  .web__rule--right { background: linear-gradient(90deg, var(--brand-mid), transparent); }
  .back-alt__facets { position: absolute; inset: 0; }
</style>
</head>
<body>

<section class="card card--front" aria-label="Business card front">
  <div class="brand">
    <div class="brand__mark"></div>
    <div class="brand__name">SilverLedgerOak</div>
    <div class="brand__tagline">Guiding growing firms and their people toward lasting success</div>
  </div>

  <div class="contact">
    <div class="contact__name">Daniel Hartley</div>
    <div class="contact__role">Director</div>
    <ul class="contact__list">
      <li class="contact__item">
        <svg class="contact__icon" viewBox="0 0 14 14"><circle cx="7" cy="7" r="7" fill="#1b1b1b"/><rect x="4.6" y="3" width="4.8" height="8" rx="1" fill="#fff"/><rect x="5.4" y="4" width="3.2" height="5" fill="#1b1b1b"/></svg>
        0412 608 935
      </li>
      <li class="contact__item">
        <svg class="contact__icon" viewBox="0 0 14 14"><circle cx="7" cy="7" r="7" fill="#1b1b1b"/><path d="M4.2 3.5l1.6-.3.9 2-1 .8a5 5 0 0 0 2.3 2.3l.8-1 2 .9-.3 1.6c-3.6.3-6.6-2.7-6.3-6.3z" fill="#fff"/></svg>
        1300 847 213
      </li>
      <li class="contact__item">
        <svg class="contact__icon" viewBox="0 0 14 14"><circle cx="7" cy="7" r="7" fill="#1b1b1b"/><rect x="3.5" y="5.5" width="7" height="4.5" fill="#fff"/><rect x="5" y="3.2" width="4" height="2.5" fill="#fff"/></svg>
        1300 847 286
      </li>
      <li class="contact__item">
        <svg class="contact__icon" viewBox="0 0 14 14"><circle cx="7" cy="7" r="7" fill="#1b1b1b"/><rect x="3.3" y="4.3" width="7.4" height="5.4" fill="#fff"/><path d="M3.3 4.3L7 7.4l3.7-3.1" stroke="#1b1b1b" stroke-width=".9" fill="none"/></svg>
        sample@silverledgeroak.com.au
      </li>
      <li class="contact__item">
        <svg class="contact__icon" viewBox="0 0 14 14"><circle cx="7" cy="7" r="7" fill="#1b1b1b"/><circle cx="7" cy="7" r="3.8" fill="none" stroke="#fff" stroke-width="1"/><path d="M3.2 7h7.6M7 3.2v7.6" stroke="#fff" stroke-width=".8"/></svg>
        www.silverledgeroak.com.au
      </li>
    </ul>
    <div class="contact__company">SilverLedgerOak</div>
    <div class="contact__address">Suite 4 - Level 3/48 Halloran Avenue<br>Kestrelvale NSW 2391</div>
  </div>

  <svg class="bands" width="540" height="40" viewBox="0 0 540 40">
    <polygon points="0,4 262,4 278,40 0,40" fill="var(--brand-blue)"/>
    <polygon points="270,4 540,4 540,16 275,16" fill="var(--navy)"/>
    <polygon points="281,22 540,22 540,34 286,34" fill="var(--brand-blue)"/>
  </svg>
</section>

<section class="card card--back" aria-label="Business card back, navy">
  <div class="back__name">SilverLedgerOak</div>
  <div class="social"><span class="social__dot"></span><span class="social__dot"></span><span class="social__dot"></span><span class="social__dot"></span></div>
  <div class="web"><span class="web__rule"></span>www.silverledgeroak.com.au<span class="web__rule web__rule--right"></span></div>
</section>

<section class="card card--back-alt" aria-label="Business card back, blue variant">
  <svg class="back-alt__facets" viewBox="0 0 540 306" preserveAspectRatio="none">
    <polygon points="0,0 160,0 60,306 0,306" fill="#ffffff" opacity=".04"/>
    <polygon points="60,60 200,20 200,306 60,306" fill="#ffffff" opacity=".05"/>
    <polygon points="360,0 540,0 540,140" fill="#000000" opacity=".12"/>
  </svg>
  <div class="back__name">SilverLedgerOak</div>
  <div class="social"><span class="social__dot"></span><span class="social__dot"></span><span class="social__dot"></span><span class="social__dot"></span></div>
  <div class="web"><span class="web__rule"></span>www.silverledgeroak.com.au<span class="web__rule web__rule--right"></span></div>
</section>

</body>
</html>
```